New Dental Office Needs an Attractive and user friendly Website Designed

I need a website for a new dental office. The Name is Maplecrest Dentistry. I would like a Modern design with a user friendly interface and usability.
I would like a landing page, a page that lists the services we offer: Cosmetic Dentistry, Implants, Dental Hygiene, Emergency Services, Restorations, Dentures
Target Market(s)
Mid to upper class
Industry/Entity Type
Dentistry
Coding
Coded - Design and coding required
Number of Pages Required
1 page
Requirements
Must have
- Landing page that has a scheduling option, Procedures, operating hours, and contact us info
Nice to have
- Appealing design, Soft comforting colors. Easy to navigate page, Modern and professional.

```html
<!DOCTYPE html>
<html lang="en">
<head>
<meta charset="utf-8">
<title>Maplecrest Dentistry</title>
<link rel="stylesheet" href="https://fonts.googleapis.com/css2?family=Domine:wght@500;700&family=Inter:wght@400;500;600&display=swap">
<style>
:root{
  --green:#74b83a;
  --green-soft:#cfe8b4;
  --ink:#1f1f1f;
  --text:#3a3a3a;
  --muted:#8a8a8a;
  --card:#f5f5f5;
  --dark:#2a2a2a;
  --white:#ffffff;
}
*{box-sizing:border-box;margin:0;padding:0}
html,body{width:1200px;height:3848px;overflow:hidden;background:var(--white)}
body{position:relative;font-family:"Inter",sans-serif;color:var(--text)}
.abs{position:absolute}
.serif{font-family:"Domine",serif;font-weight:700;color:var(--ink)}
.photo{position:absolute;border-radius:6px}
.label{position:absolute;font-size:17px;font-weight:600;letter-spacing:3px;color:var(--green);display:flex;align-items:center;gap:18px}
.label::before{content:"";width:32px;height:1.5px;background:var(--green)}
.label.center::after{content:"";width:32px;height:1.5px;background:var(--green)}
.h2{position:absolute;font-family:"Domine",serif;font-weight:700;font-size:40px;line-height:54px;color:var(--ink)}
.body{position:absolute;font-size:15px;line-height:27px;color:var(--text)}
.btn-dark{position:absolute;background:var(--ink);color:var(--white);border-radius:5px;display:flex;align-items:center;justify-content:center;gap:10px}
.btn-line{position:absolute;border:1.5px solid var(--ink);border-radius:5px;display:flex;align-items:center;justify-content:center;gap:10px;color:var(--ink);background:rgba(255,255,255,.6)}

/* nav */
.nav-home{left:91px;top:30px;width:84px;height:46px;font-size:13px;font-weight:600}
.nav-link{top:44px;font-size:13px;color:var(--ink)}
.brand{left:500px;top:30px;width:200px;text-align:center;font-family:"Domine",serif;font-weight:500;font-size:28px;color:var(--ink);line-height:46px}
.nav-phone{left:733px;top:30px;width:174px;height:46px;font-size:13px}
.nav-cta{left:925px;top:30px;width:182px;height:46px;font-size:13px}

/* hero */
.hero-bg{left:0;top:0;width:1200px;height:740px;background:linear-gradient(180deg,#eceef0 0%,#e4e6e8 45%,#f3f3f3 80%,#ffffff 100%)}
.hero-title{left:0;width:1200px;text-align:center;top:200px;font-size:90px;line-height:110px}
.hero-sub{left:0;width:1200px;text-align:center;top:314px;font-family:"Domine",serif;font-weight:500;font-size:58px;line-height:70px;color:var(--ink)}
.hero-text{left:100px;width:1000px;text-align:center;top:395px;font-size:30px;line-height:45px;color:var(--ink)}
.hero-book{left:291px;top:518px;width:299px;height:66px;font-size:20px}
.hero-explore{left:608px;top:518px;width:299px;height:66px;font-size:20px}

/* services */
.svc{position:absolute;width:324px;height:172px;background:var(--card);border-radius:8px;text-align:center}
.svc .ring{position:absolute;left:119px;top:-45px;width:86px;height:86px;border-radius:50%;border:3px solid var(--white)}
.svc h3{position:absolute;top:61px;left:0;width:100%;font-size:19px;font-weight:600;color:var(--green)}
.svc p{position:absolute;top:93px;left:30px;width:264px;font-size:15px;line-height:27px;color:var(--text)}

/* why cards */
.why{position:absolute;width:283px;height:143px;background:var(--card);border-radius:8px;padding:30px 30px}
.why h3{font-size:19px;font-weight:600;color:var(--green);margin-bottom:10px}
.why p{font-size:15px;line-height:27px;text-align:justify}

/* contact */
.ci{position:absolute;left:748px;display:flex;align-items:center;gap:14px;font-size:16px;color:var(--ink)}
.ci .dot{width:22px;height:22px;border-radius:50%;background:var(--green);display:flex;align-items:center;justify-content:center}
.hours{position:absolute;font-size:12px;color:var(--text)}

/* testimonials */
.t-text{position:absolute;width:296px;font-size:12px;line-height:21px;text-align:justify;color:var(--text)}
.t-name{position:absolute;font-size:21px;font-weight:600;color:var(--green)}
.t-time{position:absolute;font-size:12px;color:var(--muted)}
.quote{position:absolute;font-family:"Domine",serif;font-size:150px;line-height:150px;color:var(--green-soft)}

/* footer */
.footer{left:0;top:3559px;width:1200px;height:289px;background:var(--dark)}
.f-title{position:absolute;font-size:15px;font-weight:500;color:var(--white)}
.f-list{position:absolute;list-style:none;font-size:11.5px;line-height:22px;color:#e6e6e6}
.f-brand{left:91px;top:3602px;font-family:"Domine",serif;font-weight:500;font-size:24px;color:var(--white)}
.f-desc{left:91px;top:3653px;width:240px;font-size:11.5px;line-height:20px;color:#e6e6e6;text-align:justify}
.f-social{position:absolute;top:3737px;width:24px;height:24px;border-radius:4px;background:var(--green)}
.f-input{left:828px;top:3626px;width:279px;height:39px;border-radius:5px;background:var(--white);font-size:11px;color:var(--muted);padding:12px 15px}
.f-sub{left:828px;top:3677px;width:95px;height:33px;border-radius:5px;background:var(--green);color:var(--white);font-size:11px;display:flex;align-items:center;justify-content:center}
.f-rule{left:91px;top:3795px;width:1016px;height:1px;background:#6a6a6a}
.f-copy{left:0;width:1200px;top:3814px;text-align:center;font-size:11.5px;color:#e6e6e6}
</style>
</head>
<body>

<!-- hero -->
<div class="abs hero-bg" role="img" aria-label="Photo of a dentist treating a smiling patient in a bright clinic, softly faded"></div>

<div class="btn-dark nav-home">Home</div>
<div class="abs nav-link" style="left:199px">Our Services</div>
<div class="abs nav-link" style="left:304px">About Us</div>
<div class="abs nav-link" style="left:388px">Testimonials</div>
<div class="abs brand">Maplecrest Dentistry</div>
<div class="btn-line nav-phone">
  <svg width="18" height="14" viewBox="0 0 18 14"><path d="M1 5c0-3 16-3 16 0v2h-4V5H5v2H1z" fill="#1f1f1f"/><rect x="4" y="7" width="10" height="6" rx="1.5" fill="#1f1f1f"/></svg>
  +(555) 987-2140
</div>
<div class="btn-dark nav-cta">Schedule Appointment</div>

<h1 class="abs serif hero-title">Smile Brighter</h1>
<div class="abs hero-sub">with Maplecrest Dentistry</div>
<p class="abs hero-text">Personalized and professional dental care in a soothing environment for you and your family.</p>
<div class="btn-dark hero-book">
  <svg width="28" height="28" viewBox="0 0 28 28" fill="none" stroke="#fff" stroke-width="1.8"><rect x="3" y="5" width="22" height="20" rx="3"/><path d="M3 11h22M9 2v6M19 2v6"/><circle cx="9" cy="16" r=".8" fill="#fff"/><circle cx="14" cy="16" r=".8" fill="#fff"/><circle cx="19" cy="16" r=".8" fill="#fff"/><circle cx="9" cy="20" r=".8" fill="#fff"/><circle cx="14" cy="20" r=".8" fill="#fff"/></svg>
  Book an Appointment
</div>
<div class="btn-line hero-explore">Explore Our Services
  <svg width="18" height="14" viewBox="0 0 18 14" fill="none" stroke="#1f1f1f" stroke-width="1.8"><path d="M1 7h15M10 1l6 6-6 6"/></svg>
</div>

<!-- about -->
<div class="label" style="left:91px;top:748px">ABOUT US</div>
<h2 class="h2" style="left:91px;top:783px;width:560px">Welcome to Maplecrest Dentistry</h2>
<p class="body" style="left:91px;top:900px;width:585px;text-align:justify">At Maplecrest Dentistry, we provide top-tier dental care in a warm and relaxing environment. Our team of experienced professionals is dedicated to delivering personalized services using the latest technologies.</p>
<div class="abs" style="left:91px;top:1013px;font-size:14px;color:var(--muted)">Learn more &nbsp;→</div>
<div class="photo" style="left:741px;top:742px;width:366px;height:296px;background:linear-gradient(135deg,#e3d7cc,#9fb7c9 55%,#d9dfe4)" role="img" aria-label="Dentist examining a patient's teeth in the chair"></div>

<!-- services -->
<div class="label center" style="left:0;width:1200px;justify-content:center;top:1126px">OUR SERVICES</div>
<h2 class="h2" style="left:0;width:1200px;text-align:center;top:1152px">Comprehensive Dental Solutions<br>for Every Smile</h2>

<div class="svc" style="left:91px;top:1325px"><div class="ring" role="img" aria-label="Patient at a cosmetic dental consultation" style="background:linear-gradient(135deg,#cfe0ee,#e9dcd3)"></div><h3>Cosmetic Dentistry</h3><p>Enhance your smile with advanced aesthetic treatments.</p></div>
<div class="svc" style="left:438px;top:1325px"><div class="ring" role="img" aria-label="Dental implant model" style="background:linear-gradient(135deg,#f1ece8,#d8b7ab)"></div><h3>Dental Implants</h3><p>Natural-looking replacements for missing teeth.</p></div>
<div class="svc" style="left:783px;top:1325px"><div class="ring" role="img" aria-label="Smiling patient after a cleaning" style="background:linear-gradient(135deg,#c6d6e6,#eadcd2)"></div><h3>Dental Hygiene</h3><p>Preventative care for long-lasting oral health.</p></div>
<div class="svc" style="left:91px;top:1563px"><div class="ring" role="img" aria-label="Dental team performing an urgent procedure" style="background:linear-gradient(135deg,#1f3a66,#6a8fb5)"></div><h3>Emergency Services</h3><p>Fast and effective care when you need it most.</p></div>
<div class="svc" style="left:438px;top:1563px"><div class="ring" role="img" aria-label="Close-up of teeth being restored" style="background:linear-gradient(135deg,#5a2c26,#e6c9bd)"></div><h3>Restorations</h3><p>Repair and restore damaged teeth to full function.</p></div>
<div class="svc" style="left:783px;top:1563px"><div class="ring" role="img" aria-label="Hands holding a denture set" style="background:linear-gradient(135deg,#f3e6df,#d98b7a)"></div><h3>Dentures</h3><p>Comfortable and natural-looking tooth replacements.</p></div>

<!-- appointment -->
<div class="photo" style="left:91px;top:1827px;width:583px;height:327px;background:linear-gradient(120deg,#eef0f1,#dfe3e6 60%,#c9ced3)" role="img" aria-label="Dentist in a white coat standing in a treatment room"></div>
<div class="label" style="left:741px;top:1825px">APPOINTMENT</div>
<h2 class="h2" style="left:741px;top:1860px;width:380px">Ready to Smile Confidently?</h2>
<p class="body" style="left:741px;top:1977px;width:366px;text-align:justify">Scheduling an appointment with Maplecrest Dentistry is simple and stress-free. Whether you're a new or returning patient, we're here to make your dental care as convenient as possible.</p>
<div class="btn-dark" style="left:741px;top:2104px;width:275px;height:50px;font-size:14px">Book Your Appointment Now →</div>

<!-- why -->
<div class="label" style="left:91px;top:2248px">WHY CHOOSE US</div>
<h2 class="h2" style="left:91px;top:2283px;width:560px">Why Choose Maplecrest Dentistry?</h2>
<div class="why" style="left:91px;top:2404px"><h3>Trusted Professionals</h3><p>Skilled dentists with years of experience.</p></div>
<div class="why" style="left:391px;top:2404px"><h3>Relaxing Environment</h3><p>Designed for your comfort and peace of mind.</p></div>
<div class="why" style="left:91px;top:2565px"><h3>Advanced Technology</h3><p>Digital imaging, modern tools, and precision techniques.</p></div>
<div class="why" style="left:391px;top:2565px"><h3>Flexible Scheduling</h3><p>Extended hours and same-day appointments available.</p></div>
<div class="photo" style="left:741px;top:2247px;width:366px;height:462px;background:linear-gradient(160deg,#d6dde3,#9fb1c2 45%,#e2cdbf)" role="img" aria-label="Laughing patient during a dental check-up"></div>

<!-- contact -->
<div class="photo" style="left:97px;top:2801px;width:583px;height:290px;background:linear-gradient(120deg,#f3f4f5,#e4e8eb 60%,#cfd6dc)" role="img" aria-label="Smiling dentist with arms crossed beside a dental chair"></div>
<div class="label" style="left:748px;top:2801px">CONTACT US</div>
<h2 class="h2" style="left:748px;top:2834px">We're Here for You</h2>
<div class="ci" style="top:2899px"><span class="dot"><svg width="10" height="12" viewBox="0 0 10 12"><path d="M5 11S1 7 1 4.5a4 4 0 0 1 8 0C9 7 5 11 5 11z" fill="none" stroke="#fff" stroke-width="1.4"/></svg></span>48 Maplecrest Lane, City, State, ZIP</div>
<div class="ci" style="top:2934px"><span class="dot"><svg width="11" height="11" viewBox="0 0 11 11"><path d="M2 1l2 2-1 1.5a6 6 0 0 0 3.5 3.5L8 7l2 2-1.5 1.5C4 10 1 7 .5 2.5z" fill="none" stroke="#fff" stroke-width="1.2"/></svg></span>+(555) 987-2140</div>
<div class="ci" style="top:2968px"><span class="dot"><svg width="11" height="9" viewBox="0 0 11 9"><rect x=".7" y=".7" width="9.6" height="7.6" rx="1" fill="none" stroke="#fff" stroke-width="1.2"/><path d="M1 1l4.5 4L10 1" fill="none" stroke="#fff" stroke-width="1.2"/></svg></span>info@maplecrestdentistry.com</div>
<div class="ci" style="top:3004px"><span class="dot"><svg width="11" height="11" viewBox="0 0 11 11"><circle cx="5.5" cy="5.5" r="4.6" fill="none" stroke="#fff" stroke-width="1.2"/><path d="M5.5 3v2.8l2 1.2" fill="none" stroke="#fff" stroke-width="1.2"/></svg></span>Open Hours</div>
<div class="hours" style="left:784px;top:3032px">Mon – Fri</div><div class="hours" style="left:861px;top:3032px">9:00 AM – 6:00 PM</div>
<div class="hours" style="left:784px;top:3054px">Sat</div><div class="hours" style="left:861px;top:3054px">9:00 AM – 1:00 PM</div>
<div class="hours" style="left:784px;top:3075px">Sun</div><div class="hours" style="left:861px;top:3075px">Closed</div>

<!-- testimonials -->
<div class="label center" style="left:0;width:1200px;justify-content:center;top:3180px">TESTIMONIALS</div>
<h2 class="h2" style="left:0;width:1200px;text-align:center;top:3206px">What Our Patients Are Saying?</h2>

<svg class="abs" style="left:34px;top:3370px" width="16" height="28" viewBox="0 0 16 28"><path d="M14 2L2 14l12 12" fill="none" stroke="#b5b5b5" stroke-width="2"/></svg>
<svg class="abs" style="left:1149px;top:3370px" width="16" height="28" viewBox="0 0 16 28"><path d="M2 2l12 12L2 26" fill="none" stroke="#b5b5b5" stroke-width="2"/></svg>

<div class="photo" style="left:91px;top:3285px;width:167px;height:198px;background:linear-gradient(160deg,#6b4a35,#2b2521 60%,#cfc7bf)" role="img" aria-label="Portrait of a smiling female patient"></div>
<p class="t-text" style="left:287px;top:3289px">My experience at Maplecrest Dentistry was outstanding. The staff was warm and welcoming, and the clinic had a clean, calming atmosphere. Dr. Hollis was professional, explained everything clearly, and made me feel completely at ease. I finally found a dental office that truly cares about its patients.</p>
<div class="t-name" style="left:287px;top:3437px">Nora L.</div>
<div class="t-time" style="left:287px;top:3467px">10 hours ago</div>
<div class="quote" style="left:518px;top:3405px">”</div>

<div class="photo" style="left:617px;top:3285px;width:166px;height:198px;background:linear-gradient(180deg,#dfe5ea,#c8d0d7 50%,#2a2a2a)" role="img" aria-label="Portrait of a male patient outdoors"></div>
<p class="t-text" style="left:811px;top:3289px">Maplecrest Dentistry exceeded my expectations. The team was friendly, the environment was soothing, and the care I received was top-notch. I left feeling confident and well taken care of — I wouldn't go anywhere else.</p>
<div class="t-name" style="left:811px;top:3437px">Marcus T.</div>
<div class="t-time" style="left:811px;top:3467px">20 hours ago</div>
<div class="quote" style="left:1042px;top:3405px">”</div>

<!-- footer -->
<div class="abs footer"></div>
<div class="abs f-brand">Maplecrest Dentistry</div>
<p class="abs f-desc">Exceptional dental care in a calming, modern environment. We're dedicated to helping you smile with confidence through personalized, professional service.</p>

<div class="f-title" style="left:421px;top:3595px">Quick Links</div>
<ul class="f-list" style="left:421px;top:3626px"><li>Home</li><li>Our Services</li><li>About Us</li><li>Testimonials</li><li>Contact</li><li>Schedule Appointment</li></ul>

<div class="f-title" style="left:614px;top:3595px">Company</div>
<ul class="f-list" style="left:614px;top:3626px"><li>Support</li><li>Privacy policy</li><li>Terms of service</li></ul>
<div class="f-title" style="left:614px;top:3707px">Stay Connected</div>
<div class="f-social" style="left:614px"></div>
<div class="f-social" style="left:648px"></div>
<div class="f-social" style="left:682px"></div>

<div class="f-title" style="left:828px;top:3595px">Newsletter</div>
<div class="abs f-input">Write your email</div>
<div class="abs f-sub">Subscribe</div>

<div class="abs f-rule"></div>
<div class="abs f-copy">© 2025 Maplecrest Dentistry. All Rights Reserved.</div>

</body>
</html>
```